Exciting new female owned mobile Aesthetics company preparing for our first tradeshows!

We are a simple, elegant and fresh female owned concierge/mobile aesthetics company, catering to both men and women ages 30-60. We are looking for booth decoration ideas. We are a service based company that is not selling products, so we need ideas for banners and tabletop designs. We would like the design to match our logo and website colors. Website is at www(dot)fernquill(dot)com.

Target Market(s)

30-60 year old men and women, but mostly women

Industry/Entity Type

beauty and aesthetics

Font styles to use
Sans Serif
Script

Requirements
Must have
• Retractable Banner designs (33inch x 80inch) All designs need to match colors and design of logo and website at fernquill(dot)com

```html
<!DOCTYPE html>
<html lang="en">
<head>
<meta charset="utf-8">
<title>Fernquill Booth Graphics</title>
<link rel="stylesheet" href="https://fonts.googleapis.com/css2?family=Dancing+Script:wght@600;700&family=Fjalla+One&family=Roboto+Condensed:wght@700&display=swap">
<style>
  :root {
    --stage: #cdcdcd;
    --sky-deep: #2c3f9e;
    --sky-mid: #5b8fd6;
    --sky-light: #bfe3f7;
    --sky-glow: #ffffff;
    --field-gold: #e9a436;
    --field-orange: #d85a1e;
    --field-red: #b21c18;
    --field-dark: #4a1010;
    --brand-orange: #ef7a2c;
    --tag-pink: #d4157f;
    --pill-pink: #d0187f;
    --white: #ffffff;
  }
  * { box-sizing: border-box; margin: 0; padding: 0; }
  html, body { width: 1200px; height: 840px; overflow: hidden; background: var(--stage); }
  .canvas { position: relative; width: 1200px; height: 840px; }

  .panel { position: absolute; overflow: hidden; }
  .panel-sky {
    position: absolute; inset: 0;
    background:
      radial-gradient(ellipse 55% 50% at 50% 62%, var(--sky-glow) 0%, var(--sky-light) 35%, rgba(191,227,247,0) 75%),
      linear-gradient(180deg, var(--sky-deep) 0%, var(--sky-mid) 40%, var(--sky-light) 70%);
  }
  .panel-sky::after {
    content: ""; position: absolute; inset: 0;
    background: linear-gradient(90deg, rgba(20,30,110,0.35) 0%, rgba(20,30,110,0) 18%, rgba(20,30,110,0) 82%, rgba(15,25,100,0.55) 100%);
  }
  .panel-field {
    position: absolute; left: 0; right: 0; bottom: 0;
    background: linear-gradient(180deg, #f3d27a 0%, var(--field-gold) 10%, var(--field-orange) 32%, var(--field-red) 60%, var(--field-dark) 100%);
  }

  .backdrop { left: 420px; top: 110px; width: 720px; height: 620px; }
  .backdrop .panel-field { top: 383px; }

  .brand { position: absolute; display: flex; align-items: center; justify-content: center; gap: 16px; }
  .brand-mark { border-radius: 50%; background: var(--brand-orange); flex: none; }
  .brand-name {
    font-family: "Dancing Script", cursive; font-weight: 700;
    color: var(--brand-orange); line-height: 1;
  }
  .backdrop .brand { left: 0; right: 0; top: 60px; }
  .backdrop .brand-mark { width: 26px; height: 26px; }
  .backdrop .brand-name { font-size: 92px; }

  .tagline {
    position: absolute; left: 0; right: 0; top: 200px; text-align: center;
    font-family: "Dancing Script", cursive; font-weight: 600;
    color: var(--tag-pink); font-size: 36px; line-height: 1.05;
  }

  .services {
    position: absolute; left: 56px; right: 70px; top: 308px;
    display: flex; justify-content: space-between; list-style: none;
  }
  .service {
    height: 58px; padding: 0 16px 4px 12px; display: flex; align-items: center;
    background: var(--pill-pink); color: var(--white);
    font-family: "Fjalla One", sans-serif; font-size: 22px; letter-spacing: 0.2px;
    border-radius: 4px 30px 0 30px;
  }
  .service-private { width: 122px; }
  .service-group { width: 126px; }
  .service-party { width: 132px; }
  .service-events { width: 158px; }

  .web-address {
    position: absolute; right: 38px; top: 424px;
    font-family: "Roboto Condensed", sans-serif; font-weight: 700;
    color: var(--white); font-size: 30px; letter-spacing: -0.3px;
  }

  .counter { left: 80px; top: 320px; width: 250px; height: 410px; }
  .counter .panel-field { top: 270px; }
  .counter .brand { left: 0; right: 0; top: 160px; gap: 8px; }
  .counter .brand-mark { width: 12px; height: 12px; }
  .counter .brand-name { font-size: 46px; }
</style>
</head>
<body>
<main class="canvas">

  <section class="panel counter" aria-label="Counter wrap">
    <div class="panel-sky" role="img" aria-label="Photo of a blue sky glowing at the horizon"></div>
    <div class="panel-field" role="img" aria-label="Photo of a red poppy field at sunrise"></div>
    <div class="brand">
      <span class="brand-mark"></span>
      <span class="brand-name">Fernquill</span>
    </div>
  </section>

  <section class="panel backdrop" aria-label="Booth backdrop">
    <div class="panel-sky" role="img" aria-label="Photo of a blue sky glowing at the horizon"></div>
    <div class="panel-field" role="img" aria-label="Photo of a red poppy field at sunrise"></div>

    <div class="brand">
      <span class="brand-mark"></span>
      <span class="brand-name">Fernquill</span>
    </div>

    <p class="tagline">Live life on your own time<br>Fernquill comes to you!</p>

    <ul class="services">
      <li class="service service-private">Private Session</li>
      <li class="service service-group">Group Session</li>
      <li class="service service-party">Fernquill Party</li>
      <li class="service service-events">Upcoming Events</li>
    </ul>

    <p class="web-address">www.fernquill.com</p>
  </section>

</main>
</body>
</html>
```